New healthy snacks brand

We are launching a brand new product with an innovative new concept.
The product is an outer carton box which contains 4 inner plastic punnets, each containing a different type of dry snack.
The brand identity is, healthy, environmentally friendly, convenient, simple and cool. The target customers are 25-50 year old healthy conscious medium to high income office workers.
The name is amber wayfare.

Outer box:
The outer box will be made of brown recycled carton. The dimensions are to be approximately that of an A4 paper, 21cmX30cmX3cm height.
The top side of the cover is to be as uncluttered as possible and to contain only the logo and the recyclable symbol.

The inside of the top cover is to contain a drawing/picture relevant to the brand identity.
The bottom side is to contain the following:
-The top left area of 4 cm X 10 cm is to be left blank to allow for a sticker with address, and name of the recipient of this specific box.
- The top right area (4cm X 20cm) is to contain mini logos for the following claims along with the wording itself:
- Gluten free - Cholesterol free - Soy free - Lactose free - natural - vegan - No high fructose corn syrup - No artificial flavours - 0g transfat - No artificial sweeteners - no partially hydrogenated oil.

Inner containers:
There will be 4 inner plastic containers arranged in a square formation (see pictures). Each container is to have a transparent label adhered to its oval top containing the following:
- Brand logo
- Name of the type of snack inside.
- The barcode
-In fine print the list if ingredients.
- The printing is to be in one colour only to allow ease of viewing the contents of the punnet.
For more clarifications please see the attached pictures of the blank packaging samples.

Target Market(s)

25 - 50 year old healthy conscious professionals.

Industry/Entity Type

Plastic

Requirements
Must have
• The design must be as simple as possible using one maximum 2 earthy colours.

```html
<!DOCTYPE html>
<html lang="en">
<head>
<meta charset="utf-8">
<title>amber wayfare – outer box, back panel</title>
<link rel="stylesheet" href="https://fonts.googleapis.com/css2?family=Bangers&family=Arimo:wght@400&family=PT+Sans:wght@400&display=swap">
<style>
  :root {
    --page: #ffffff;
    --ink: #000000;
    --kraft: #87694c;
    --kraft-light: #8f7254;
    --kraft-dark: #7c5f43;
    --kraft-edge: #4a3a2a;
    --claim-yellow: #f4ec7c;
    --leaf-green: #8cc63f;
    --back-brown: #8b6a4f;
  }
  * { margin: 0; padding: 0; box-sizing: border-box; }
  html, body { width: 1200px; height: 841px; overflow: hidden; background: var(--page); }
  .sheet { position: relative; width: 1200px; height: 841px; font-family: "Arimo", Arial, sans-serif; color: var(--ink); }

  .note { position: absolute; font-size: 14px; line-height: 18px; }
  .note-sticker { left: 155px; top: 33px; }
  .note-question { left: 4px; top: 474px; width: 100px; }
  .note-question p + p { margin-top: 16px; }

  .bracket { position: absolute; }
  .bracket-sticker { left: 193px; top: 78px; width: 284px; height: 25px; border: 1px solid var(--ink); border-bottom: none; }
  .bracket-empty { left: 118px; top: 284px; width: 24px; height: 460px; border: 1px solid var(--ink); border-right: none; }

  .box-back {
    position: absolute; left: 164px; top: 121px; width: 897px; height: 628px;
    background: radial-gradient(ellipse at 40% 40%, var(--kraft-light), var(--kraft) 60%, var(--kraft-dark));
    border: 1px solid var(--kraft-edge);
  }

  .address-zone {
    position: absolute; left: 29px; top: 36px; width: 282px; height: 104px;
    border: 1px solid var(--leaf-green);
    display: flex; align-items: center; justify-content: center;
    color: var(--leaf-green); font-size: 20px;
  }

  .claims {
    position: absolute; top: 28px; list-style: none;
    font-family: "Bangers", "Arial Narrow", sans-serif; font-size: 15px; letter-spacing: 0.5px;
    line-height: 21.5px; color: var(--claim-yellow); text-transform: uppercase;
  }
  .claims li::before { content: "· "; }
  .claims-left { left: 351px; }
  .claims-right { left: 502px; }

  .brand-mark {
    position: absolute; left: 744px; top: 50px; width: 122px;
    display: flex; flex-direction: column; align-items: center; gap: 6px;
    font-family: "Bangers", "Arial Narrow", sans-serif; font-size: 30px; line-height: 30px;
    color: var(--claim-yellow); text-align: center;
  }
  .brand-mark .brand-dot { width: 14px; height: 14px; border-radius: 50%; background: var(--leaf-green); }

  .panel-label {
    position: absolute; left: 968px; top: 794px;
    font-family: "PT Sans", Arial, sans-serif; font-size: 31px; color: var(--back-brown);
  }
</style>
</head>
<body>
<div class="sheet">
  <div class="note note-sticker">Smaller than your dimension to be hide behind the address sticker.</div>
  <div class="bracket bracket-sticker"></div>

  <div class="note note-question">
    <p>Question:</p>
    <p>Why should this part to be empty?</p>
  </div>
  <div class="bracket bracket-empty"></div>

  <section class="box-back" aria-label="Outer box back panel, brown recycled kraft carton">
    <div class="address-zone">address sticker here</div>

    <ul class="claims claims-left">
      <li>Gluten free</li>
      <li>Cholesterol free</li>
      <li>Soy free</li>
      <li>Lactose free</li>
      <li>Natural</li>
      <li>Vegan</li>
    </ul>
    <ul class="claims claims-right">
      <li>No high fructose corn syrup</li>
      <li>No artificial flavours</li>
      <li>0g trans-fat</li>
      <li>No artificial sweeteners</li>
      <li>No partially hydrogenated oil</li>
    </ul>

    <div class="brand-mark">
      <span class="brand-dot"></span>
      <span class="brand-name">amber wayfare</span>
    </div>
  </section>

  <div class="panel-label">BACK</div>
</div>
</body>
</html>
```